Banner for a National Dental Conference

We need a banner logo for our next Dental Conference in 2017. Our theme is 'Challenging the Status Quo'.
It must have the words '20 years of oral health therapy in Victoria' and the conference date and venue:
7-8th April 2017
Bramwell The Orchards Resort, Torquay, Victoria.
It must also feature our association logo as attached.
Please be creative, however, we would like a 'clean' design, not cluttered.
The design is intended for use in the conference program and website.

Target Market(s)

Dental practitioners

Industry/Entity Type

Dental

Requirements
Must have
• As above.

```html
<!DOCTYPE html>
<html lang="en">
<head>
<meta charset="utf-8">
<title>Challenging the Status Quo – Conference Banner</title>
<link rel="stylesheet" href="https://fonts.googleapis.com/css2?family=Dosis:wght@400&family=Raleway:wght@400;500&family=Open+Sans:wght@400;600&display=swap">
<style>
  :root {
    --page-bg: #f1f1f2;
    --banner-white: #ffffff;
    --brand-purple: #4b2a8c;
    --panel-purple-light: #5c2f9a;
    --panel-purple-dark: #3a166f;
    --accent-teal: #2fd3b4;
    --pill-green-top: #3cc597;
    --pill-green-bottom: #17916a;
    --text-light: #ffffff;
    --photo-light: #f5eee9;
    --photo-mid: #dcb79f;
    --photo-dark: #5e3f2c;
  }
  * { box-sizing: border-box; margin: 0; padding: 0; }
  html, body {
    width: 1027px;
    height: 1200px;
    overflow: hidden;
    background: var(--page-bg);
  }
  .board {
    position: relative;
    width: 1027px;
    height: 1200px;
  }
  .banner {
    position: absolute;
    width: 56.56em;
    height: 14.625em;
    background: var(--banner-white);
    overflow: hidden;
  }
  .banner--large { left: 60px; top: 358px; font-size: 16px; }
  .banner--small { left: 159px; top: 687px; font-size: 12.53px; }

  .association-name {
    position: absolute;
    left: 1.45em;
    top: 50%;
    transform: translateY(-50%);
    width: 11.5em;
    text-align: center;
    font-family: "Raleway", sans-serif;
    font-weight: 500;
    font-size: 1em;
    color: var(--brand-purple);
  }
  .association-name span {
    font-size: 2.75em;
    letter-spacing: 0.02em;
  }

  .portrait {
    position: absolute;
    left: 13.06em;
    top: 0;
    width: 20.5em;
    height: 100%;
    background:
      radial-gradient(ellipse 32% 48% at 45% 45%, var(--photo-mid) 0%, rgba(220,183,159,0.6) 60%, rgba(220,183,159,0) 100%),
      linear-gradient(90deg, var(--photo-light) 0%, #e7cdbb 35%, var(--photo-dark) 75%, #3e2a1e 100%);
  }

  .panel-shape {
    position: absolute;
    inset: 0;
    width: 100%;
    height: 100%;
  }

  .event-info {
    position: absolute;
    left: 32.3em;
    right: 0;
    top: 0;
    bottom: 0;
    color: var(--text-light);
    text-align: center;
  }
  .event-info > * {
    position: absolute;
    left: 0;
    right: 0;
    line-height: 1;
  }
  .theme-lead {
    top: 0.55em;
    font-family: "Dosis", sans-serif;
    font-weight: 400;
    font-size: 1.9em;
    color: var(--accent-teal);
    letter-spacing: 0.01em;
  }
  .theme-main {
    top: 1.07em;
    font-family: "Raleway", sans-serif;
    font-weight: 400;
    font-size: 2.85em;
    letter-spacing: 0.03em;
  }
  .anniversary {
    top: 6.5em;
    left: 50%;
    right: auto;
    width: 16em;
    height: 3.6em;
    transform: translateX(-50%);
    display: flex;
    align-items: center;
    justify-content: center;
    border-radius: 0.7em;
    border: 1px solid rgba(255,255,255,0.35);
    background: linear-gradient(180deg, var(--pill-green-top) 0%, var(--pill-green-bottom) 100%);
    font-family: "Open Sans", sans-serif;
    font-size: 1em;
  }
  .anniversary span {
    font-size: 1.1em;
    line-height: 1.2;
  }
  .event-date {
    top: 9.1em;
    font-family: "Open Sans", sans-serif;
    font-weight: 600;
    font-size: 1.2em;
  }
  .event-venue {
    top: 17.8em;
    font-family: "Open Sans", sans-serif;
    font-weight: 400;
    font-size: 0.72em;
  }
</style>
</head>
<body>
<main class="board">

  <section class="banner banner--large" aria-label="Conference banner, large">
    <div class="association-name"><span>ORALIS</span></div>
    <div class="portrait" role="img" aria-label="Photo of a smiling young woman with long wavy hair, hands at her cheeks"></div>
    <svg class="panel-shape" viewBox="0 0 705 182" preserveAspectRatio="none" aria-hidden="true">
      <defs>
        <radialGradient id="panelGlowLarge" cx="0.45" cy="0.45" r="0.7">
          <stop offset="0" stop-color="var(--panel-purple-light)"/>
          <stop offset="1" stop-color="var(--panel-purple-dark)"/>
        </radialGradient>
      </defs>
      <path d="M393 0 C414 55 420 120 410 182 L705 182 L705 0 Z" fill="#ffffff"/>
      <path d="M400 0 C421 55 427 120 417 182 L705 182 L705 0 Z" fill="url(#panelGlowLarge)"/>
    </svg>
    <div class="event-info">
      <p class="theme-lead">CHALLENGING THE</p>
      <h1 class="theme-main">STATUS QUO</h1>
      <p class="anniversary"><span>20 years of oral health<br>therapy in Victoria</span></p>
      <p class="event-date">7-8th April 2017</p>
      <p class="event-venue">Bramwell The Orchards Resort, Torquay, Victoria</p>
    </div>
  </section>

  <section class="banner banner--small" aria-label="Conference banner, small">
    <div class="association-name"><span>ORALIS</span></div>
    <div class="portrait" role="img" aria-label="Photo of a smiling young woman with long wavy hair, hands at her cheeks"></div>
    <svg class="panel-shape" viewBox="0 0 705 182" preserveAspectRatio="none" aria-hidden="true">
      <defs>
        <radialGradient id="panelGlowSmall" cx="0.45" cy="0.45" r="0.7">
          <stop offset="0" stop-color="var(--panel-purple-light)"/>
          <stop offset="1" stop-color="var(--panel-purple-dark)"/>
        </radialGradient>
      </defs>
      <path d="M393 0 C414 55 420 120 410 182 L705 182 L705 0 Z" fill="#ffffff"/>
      <path d="M400 0 C421 55 427 120 417 182 L705 182 L705 0 Z" fill="url(#panelGlowSmall)"/>
    </svg>
    <div class="event-info">
      <p class="theme-lead">CHALLENGING THE</p>
      <h2 class="theme-main">STATUS QUO</h2>
      <p class="anniversary"><span>20 years of oral health<br>therapy in Victoria</span></p>
      <p class="event-date">7-8th April 2017</p>
      <p class="event-venue">Bramwell The Orchards Resort, Torquay, Victoria</p>
    </div>
  </section>

</main>
</body>
</html>
```